Brevane Advisory business card

Premium business card required
I have attached the brand as a powerpoint template but this can be made to look very up market, I have also attached my BIO for title reasons and to give you a feel for my skills
front of card
Darrel Voskuij
Managing Director Brevane Advisory
Retail, Customer-Led Experience, Transformation and Maximising Shareholder Return
Mobile +61(0)487395028
Email darrelbrevaneadvisory.example
back of card

BREVANE ADVISORY’ OFFERING

We transform customer environments to extract benefits while elevating service levels;
We release millions of dollars in self-funding through continuous improvement;
We see CX as a key differentiator, proactively guarding share from market disrupters;
We re-invent service and create front-end of the future.

```html
<!DOCTYPE html>
<html lang="en">
<head>
<meta charset="utf-8">
<title>Brevane Advisory business card</title>
<link href="https://fonts.googleapis.com/css2?family=Montserrat:wght@400;500;600&family=Open+Sans:wght@400;600&display=swap" rel="stylesheet">
<style>
  :root {
    --backdrop: #e6e4e1;
    --card-dark: #111112;
    --card-light: #ffffff;
    --ink-grey: #7b7b7d;
    --ink-dark: #3c3c3e;
    --ink-muted: #a9a9ab;
    --ink-light: #e9e9ea;
    --frame-grey: #8a8a8c;
  }
  * { box-sizing: border-box; margin: 0; padding: 0; }
  html, body { width: 1200px; height: 715px; overflow: hidden; }
  body {
    background: var(--backdrop);
    display: flex;
    align-items: center;
    justify-content: center;
    gap: 56px;
    font-family: "Open Sans", sans-serif;
  }
  .card {
    width: 520px;
    height: 297px;
    position: relative;
    box-shadow: 0 10px 28px rgba(0,0,0,.22);
  }
  .card--back { background: var(--card-dark); color: var(--ink-light); }
  .card--front { background: var(--card-light); color: var(--ink-dark); }

  .brand {
    position: absolute;
    top: 34px;
    left: 40px;
    display: flex;
    align-items: center;
    gap: 10px;
    font-family: "Montserrat", sans-serif;
    font-weight: 600;
    font-size: 22px;
    letter-spacing: .04em;
    color: var(--frame-grey);
  }
  .brand__square {
    width: 18px;
    height: 18px;
    background: var(--frame-grey);
  }
  .card--back .brand { color: #5e5e60; }
  .card--back .brand__square { background: #5e5e60; }

  .offering {
    position: absolute;
    left: 40px;
    right: 36px;
    top: 112px;
  }
  .offering__title {
    font-family: "Montserrat", sans-serif;
    font-weight: 500;
    font-size: 12.5px;
    letter-spacing: .03em;
    color: var(--ink-muted);
    margin-bottom: 14px;
  }
  .offering__list { list-style: none; }
  .offering__list li {
    position: relative;
    padding-left: 13px;
    font-size: 10.5px;
    line-height: 1.55;
    color: var(--ink-light);
  }
  .offering__list li::before {
    content: "";
    position: absolute;
    left: 0;
    top: 6px;
    width: 5px;
    height: 5px;
    border-radius: 50%;
    background: var(--ink-muted);
  }

  .contact {
    position: absolute;
    left: 40px;
    top: 112px;
  }
  .contact__name {
    font-family: "Montserrat", sans-serif;
    font-weight: 500;
    font-size: 17px;
    letter-spacing: .03em;
    text-transform: uppercase;
    color: var(--ink-grey);
  }
  .contact__role,
  .contact__company {
    font-size: 13px;
    line-height: 1.35;
    color: var(--ink-dark);
  }
  .contact__role { margin-top: 3px; }
  .contact__lines { margin-top: 18px; list-style: none; }
  .contact__lines li {
    display: flex;
    align-items: center;
    gap: 9px;
    font-size: 13px;
    line-height: 1.55;
    color: var(--ink-dark);
  }
  .contact__icon { width: 11px; height: 11px; flex: none; }
</style>
</head>
<body>

  <section class="card card--back" aria-label="Back of card">
    <div class="brand"><span class="brand__square"></span>Brevane Advisory</div>
    <div class="offering">
      <h2 class="offering__title">BREVANE ADVISORY’ OFFERING</h2>
      <ul class="offering__list">
        <li>We transform customer environments to extract benefits while elevating service levels;</li>
        <li>We release millions of dollars in self-funding through continuous improvement;</li>
        <li>We see CX as a key differentiator, proactively guarding share from market disrupters;</li>
        <li>We re-invent service and create front-end of the future.</li>
      </ul>
    </div>
  </section>

  <section class="card card--front" aria-label="Front of card">
    <div class="brand"><span class="brand__square"></span>Brevane Advisory</div>
    <div class="contact">
      <h1 class="contact__name">Darrel Voskuij</h1>
      <p class="contact__role">Managing Director</p>
      <p class="contact__company">Brevane Advisory</p>
      <ul class="contact__lines">
        <li>
          <svg class="contact__icon" viewBox="0 0 24 24" aria-hidden="true"><path fill="#8a8a8c" d="M6.6 10.8a15.1 15.1 0 0 0 6.6 6.6l2.2-2.2a1 1 0 0 1 1-.25 11.4 11.4 0 0 0 3.6.57 1 1 0 0 1 1 1V20a1 1 0 0 1-1 1A17 17 0 0 1 3 4a1 1 0 0 1 1-1h3.5a1 1 0 0 1 1 1c0 1.25.2 2.45.57 3.6a1 1 0 0 1-.25 1z"/></svg>
          +61(0)487395028
        </li>
        <li>
          <svg class="contact__icon" viewBox="0 0 24 24" aria-hidden="true"><rect x="2" y="5" width="20" height="14" rx="1.5" fill="none" stroke="#8a8a8c" stroke-width="2"/><path d="M3 6l9 7 9-7" fill="none" stroke="#8a8a8c" stroke-width="2"/></svg>
          darrelbrevaneadvisory.example
        </li>
      </ul>
    </div>
  </section>

</body>
</html>
```